business card design - photography

I am a fine art photographer. I would like to approach galleries to exhibit my work and need a business card.

The card should convey creativity and simplicity.
I would like a double sided card.

Some options:
1. An all white card with raised or embossed text or design to create a tactile finish.
2. a white and dark grey design would also work well.
3. Would be great to use my name as part of the design but not essential.
4. My name and title on the front, other details on the back of card.

The final design should be simple, minimal, elegant and innovative.
Being minimal, it will be more about texture, text size and placement.

examples of designs I would prefer provided here:
http://layoutmuse.net/ideas/40-plain-and-graceful-calling-card-layouts

I'm also open to other designs that may be unusual and unique.

Love this:
http://www.snapvault.com/pics/morningverses/583017264
Updates

I have uploaded a psd file after playing around in photoshop with various fonts.  I like the font (which I downloaded from typeshelf.net called Arual) but the design probably needs some refining.  I hope this helps.  If you'd like me to change the format of the file, please let me know.

Marta

Target Market(s)

Art Gallery owners/administrators and customers.

Industry/Entity Type

Business

Requirements
Must have
• A unique look.

Matte, silky finish or heavy textured stock. Double-sided card.

Front:
my name
photography by

Back:
phone no
email
web address
Nice to have
• Letterpress
embrossed
Clean fonts
Should not have
• Do not use illustrations of cameras or lenses.
No frames around the card edge.

```html
<!DOCTYPE html>
<html lang="en">
<head>
<meta charset="utf-8">
<title>Marta Halvern Photography – Business Card</title>
<link rel="stylesheet" href="https://fonts.googleapis.com/css2?family=Nunito:wght@900&family=Raleway:wght@400&family=Questrial&display=swap">
<style>
  :root {
    --paper: #ffffff;
    --charcoal: #1f2222;
    --ink: #1f2222;
    --light-ink: #f1f1f1;
    --split: 517px;
  }
  html, body {
    margin: 0;
    padding: 0;
    overflow: hidden;
    background: var(--paper);
  }
  .card {
    position: relative;
    width: 1033px;
    height: 1200px;
    background: var(--paper);
    overflow: hidden;
  }
  .card__dark-band {
    position: absolute;
    top: 0;
    left: var(--split);
    width: calc(1033px - var(--split));
    height: 1200px;
    background: var(--charcoal);
  }
  .brand {
    position: absolute;
    left: 0;
    top: 0;
    width: 1100px;
    height: 1200px;
    text-align: center;
  }
  .brand--light {
    clip-path: inset(0 0 0 var(--split));
  }
  .brand__name {
    position: absolute;
    left: 0;
    width: 100%;
    top: 580px;
    margin: 0;
    font-family: "Nunito", sans-serif;
    font-weight: 900;
    font-size: 118px;
    line-height: 1;
    letter-spacing: -3px;
    color: var(--ink);
  }
  .brand__title {
    position: absolute;
    left: 0;
    width: 100%;
    top: 733px;
    margin: 0;
    padding-left: 0;
    font-family: "Raleway", sans-serif;
    font-weight: 400;
    font-size: 28px;
    line-height: 1;
    letter-spacing: 24px;
    text-indent: -10px;
    color: var(--ink);
  }
  .brand--light .brand__name,
  .brand--light .brand__title {
    color: var(--paper);
  }
  .contact {
    position: absolute;
    left: 549px;
    top: 830px;
    margin: 0;
    padding: 0;
    list-style: none;
    font-family: "Questrial", sans-serif;
    font-size: 27px;
    color: var(--light-ink);
  }
  .contact__item {
    display: flex;
    align-items: center;
    height: 49px;
  }
  .contact__icon {
    width: 26px;
    height: 26px;
    margin-right: 14px;
    flex: none;
  }
</style>
</head>
<body>
  <main class="card">
    <div class="card__dark-band"></div>

    <div class="brand brand--dark" aria-hidden="true">
      <p class="brand__name">Marta Halvern</p>
      <p class="brand__title">PHOTOGRAPHY</p>
    </div>
    <div class="brand brand--light">
      <h1 class="brand__name">Marta Halvern</h1>
      <p class="brand__title">PHOTOGRAPHY</p>
    </div>

    <ul class="contact">
      <li class="contact__item">
        <svg class="contact__icon" viewBox="0 0 26 26" aria-hidden="true">
          <path d="M2 9 C2 4 24 4 24 9 L24 11 L18 11 L18 8 L8 8 L8 11 L2 11 Z" fill="#f1f1f1"/>
          <path d="M5 13 L9 10 L17 10 L21 13 L21 21 L5 21 Z" fill="#f1f1f1"/>
          <circle cx="13" cy="16" r="2.6" fill="#1f2222"/>
        </svg>
        <span>0400 555 218</span>
      </li>
      <li class="contact__item">
        <svg class="contact__icon" viewBox="0 0 26 26" aria-hidden="true">
          <rect x="1" y="6" width="24" height="15" fill="#f1f1f1"/>
          <path d="M1 6 L13 15 L25 6 M1 21 L10 13 M25 21 L16 13" stroke="#1f2222" stroke-width="1.4" fill="none"/>
        </svg>
        <span>mhalvern@inboxly.com</span>
      </li>
      <li class="contact__item">
        <svg class="contact__icon" viewBox="0 0 26 26" aria-hidden="true">
          <g fill="none" stroke="#f1f1f1" stroke-width="1.4">
            <circle cx="13" cy="13" r="11"/>
            <ellipse cx="13" cy="13" rx="5" ry="11"/>
            <line x1="13" y1="2" x2="13" y2="24"/>
            <line x1="2" y1="13" x2="24" y2="13"/>
            <path d="M4 7.5 H22 M4 18.5 H22"/>
          </g>
        </svg>
        <span>www.martahalvern.com</span>
      </li>
    </ul>
  </main>
</body>
</html>
```